Private practice for psychiatry and psychotherapy needs a business card and logo

I need a logo and business card design for my private practice for psychiatry and psychotherapy. The optional names for my practice are: Vornhoute Praktijk voor Psychiatrie en Psychotherapie, or short: Praktijk Vornhoute.
I am a (child and adolescent) psychiatrist and psychotherapist. I diagnose and treat infants, children, adolescents and adults with psychiatric symptoms/disorders. I also give supervision to colleagues about their own treatments. My work is characterised by personal involvement, transparence, creativity and professionality.
I would like to have an appealing, light and bright, yet basic design that invites people (both children and adults) to contact me, gives trust and hope, without loosing professional appearance.
I uploaded my contact information which should not necessarily be all included (in this form) on the card as long as people know how to contact me. Please feel free to be creative!
Please note that my website is only temporarely and need a new design and update too!

Target Market(s)

Clients and patients (children, adolescents, adults) with psychiatric symptoms who need diagnosis and treatment. I work with private clients and patients through medical insurances.

Industry/Entity Type

Mental Health

Contact Information for Business Card

Dr. Sanne Vornhoute-ter Kuilen
Psychiater/Kinder- en Jeugdpsychiater
Wouter Heskampstraat 14
3071 PX Rotterdam
t: 06-51928764
e: info@praktijkvornhoute.nl
i: www.praktijkvornhoute.nl

Logo Text

Praktijk Vornhoute voor Psychiatrie en Psychotherapie; or short: Praktijk Vornhoute

Font styles to use
Sans Serif
Other font styles liked:
• up to designer

Requirements
Must have
• Appealing, light, bright, creative, trustful, professional and unique.

```html
<!DOCTYPE html>
<html lang="nl">
<head>
<meta charset="utf-8">
<title>Praktijk Vornhoute – visitekaartje</title>
<link rel="stylesheet" href="https://fonts.googleapis.com/css2?family=Raleway:wght@400;500;700&display=swap">
<style>
  :root {
    --teal: #3aa69b;
    --teal-deep: #2f9a8f;
    --sun: #fec418;
    --paper: #ffffff;
    --stage: #e7e7e7;
    --muted: #8d8d8d;
  }
  * { box-sizing: border-box; margin: 0; padding: 0; }
  html, body { width: 1200px; height: 1200px; overflow: hidden; }
  body {
    background: var(--stage);
    font-family: "Raleway", Arial, sans-serif;
    position: relative;
  }
  .card {
    position: absolute;
    width: 620px;
    height: 400px;
    box-shadow: 0 2px 6px rgba(0,0,0,0.08);
  }
  .card--front {
    left: 90px; top: 110px;
    background: var(--paper);
    display: flex; align-items: center; justify-content: center;
  }
  .brand { display: flex; align-items: center; gap: 22px; }
  .brand__square {
    width: 140px; height: 140px;
    background: var(--teal);
  }
  .brand__name {
    color: var(--teal);
    font-weight: 700;
    font-size: 40px;
    line-height: 1;
  }
  .card--back {
    left: 490px; top: 650px;
    background: var(--teal);
    color: #fff;
    padding: 0 62px 70px 0;
    display: flex; flex-direction: column; justify-content: flex-end; align-items: flex-end;
    text-align: right;
  }
  .person__name { font-weight: 700; font-size: 26px; line-height: 1.2; }
  .person__role { color: var(--sun); font-weight: 400; font-size: 25px; line-height: 1.2; margin-bottom: 36px; }
  .contact { font-size: 20px; line-height: 1.36; font-weight: 400; }
  .contact b { font-weight: 700; }
  .spec {
    position: absolute;
    right: 110px; top: 420px;
    text-align: right;
    font-size: 33px; line-height: 1.15; font-weight: 500;
  }
  .spec__sun { color: var(--sun); }
  .spec__teal { color: var(--teal-deep); }
  .spec__font { color: var(--muted); }
</style>
</head>
<body>
  <section class="card card--front" aria-label="Voorkant visitekaartje">
    <div class="brand">
      <div class="brand__square"></div>
      <div class="brand__name">Praktijk<br>Vornhoute</div>
    </div>
  </section>

  <aside class="spec">
    <div class="spec__sun">Colorset 115U</div>
    <div class="spec__teal">Colorset 326U</div>
    <div class="spec__font">Font: Raleway</div>
  </aside>

  <section class="card card--back" aria-label="Achterkant visitekaartje">
    <div class="person__name">Dr. Sanne Vornhoute-ter Kuilen</div>
    <div class="person__role">Psychiater/Kinder - en Jeugdpsychiater</div>
    <div class="contact">
      Wouter Heskampstraat 14<br>
      3071 PX Rotterdam<br>
      <b>t:</b> 06-51928764<br>
      <b>e:</b> info@praktijkvornhoute.nl<br>
      <b>i:</b> www.praktijkvornhoute.nl
    </div>
  </section>
</body>
</html>
```